Geek Pagoda home page design

I'd like to take quirkvault.com existing home page and use the logo attached and make and the home page look like brainbazaar.com home page or foreverimp.com. The font size of the buttons should be similar to brainbazaar.com. does this make sense?
I've added a mock up of the layout design. I'm looking for fun nerd like design on the left and right of the borders. It should be faint but visible and add more character to the site apart from just a solid black thick border. We'd like the Glasses to be a Favicon as well.
Getting better. Let's try the logo in the top middle of the page and make sure it is bigger than the banner to the left and right. Add maybe the search bar to the left and the shipping info to the right of the log pyramid. if you do this right the pyramid will look like a nose and the surrounding rectangles will look like the glasses inside the logo we have.
Can you make the robots look like the orbit cinema gallery robots? They were the shadows of three robots at the bottom right of the tv show and they were watching movies and commenting on them. It may be a nice touch to have the robots looking at the site instead of at us the shopper from the bottom right.
Can you experiment with the side columns with what the inside of a temple may look like. Maybe some Egyptian columns with torches hanging from them.
Also can we try less pastel colors and more bold primary colors. Maybe experiment with Orange or a darker bolder blue?
Nice work. Also please correct spelling of "Customer" in the bar. And can you add a Q Roll feature in the middle above the products? this is where five featured products will rotate like a QRoll works
Updates
Project Deadline Extended
Reason: We have the holiday coming up and I guaranteed payment so we would like to see some quality work.
Target Market(s)
Target Market is young Moms, College Students and kids
Industry/Entity Type
Shipping
Look and feel
Each slider illustrates characteristics of the customer's brand and the style your logo design should communicate.

```html
<!DOCTYPE html>
<html lang="en">
<head>
<meta charset="utf-8">
<title>Geek Pagoda</title>
<link rel="stylesheet" href="https://fonts.googleapis.com/css2?family=Encode+Sans+Condensed:wght@300;400;600&display=swap">
<style>
:root{
  --blue-light:#7cc3ea;
  --blue-mid:#4a9fd6;
  --blue-dark:#1572c8;
  --green:#3fe38f;
  --panel-grey:#9b9b9b;
  --text-grey:#555;
  --white:#fff;
  --footer:#b1e8d2;
  --bg-top:#f4f4f4;
  --bg-bottom:#6fcfa9;
}
*{margin:0;padding:0;box-sizing:border-box}
html,body{width:1200px;height:960px;overflow:hidden}
body{
  position:relative;
  font-family:"Encode Sans Condensed",sans-serif;
  font-weight:300;
  color:var(--text-grey);
  background:
    repeating-linear-gradient(135deg,rgba(255,255,255,.3) 0 28px,rgba(255,255,255,0) 28px 56px),
    linear-gradient(180deg,var(--bg-top) 0%,#e9efee 40%,var(--bg-bottom) 100%);
}
.abs{position:absolute}
.top-links{right:157px;top:22px;font-size:12px;color:#333;word-spacing:2px;white-space:nowrap}
.brand{left:128px;top:100px;display:flex;align-items:center;gap:10px;font-size:30px;font-weight:600;color:#111}
.brand .mark{width:22px;height:22px;background:#111}
.nav-main{left:124px;top:211px;width:919px;height:83px;background:linear-gradient(180deg,var(--blue-light),var(--blue-mid));display:flex;align-items:center;font-size:28px;color:var(--white)}
.nav-main a{flex:1;text-align:center;text-decoration:none;color:inherit;white-space:nowrap}
.nav-main .home{flex:0 0 167px;height:100%;display:flex;align-items:center;justify-content:center;background:linear-gradient(180deg,var(--blue-mid),var(--blue-dark))}
.nav-sub{left:124px;top:294px;width:919px;height:43px;background:var(--green);border-radius:0 0 8px 8px;display:flex;align-items:center;justify-content:space-around;font-size:23px;color:#333}
.content{left:160px;top:337px;width:849px;height:574px;background:var(--white)}
.side{background:var(--panel-grey);border-radius:5px;color:var(--white)}
.side-left{left:120px;top:380px;width:163px;height:485px;padding:14px 12px}
.side-left label{font-size:12px;display:block}
.field{height:15px;background:var(--white);border-radius:8px;margin-top:4px}
.btn{display:inline-block;background:var(--green);color:#333;font-size:12px;padding:0 8px;border-radius:8px}
.cat-title{font-size:21px;font-weight:600;margin-top:4px;line-height:24px}
.cat-list{list-style:none;font-size:21px}
.cat-list li{line-height:21px;height:21px}
.cat-list li::before{content:"➡";display:inline-block;font-size:14px;line-height:1;margin-right:3px;vertical-align:middle}
.divider{border-top:1px solid #b5b5b5;margin:48px 0 18px}
.side-right{left:879px;top:374px;width:163px;height:485px;padding:28px 0 0 24px}
.side-right h2{font-weight:300;font-size:23px;line-height:28px;padding-bottom:6px;border-bottom:1px solid #b5b5b5;width:125px;white-space:nowrap}
.np{font-size:12px;line-height:15px;padding:8px 0 6px;border-bottom:1px solid #b5b5b5;width:122px;white-space:nowrap}
.card{background:var(--white);border:1px solid #d3d3d3;border-radius:8px;width:151px}
.card .ph{position:absolute;border-radius:1px}
.card .info{position:absolute;left:13px;font-size:16px;line-height:21px;white-space:nowrap}
.card .info.sm{font-size:11px;line-height:15px}
.footer{left:161px;top:922px;width:844px;height:26px;background:var(--footer);border-radius:6px;font-size:13px;color:#333;padding:5px 6px}
</style>
</head>
<body>
<div class="abs top-links">My Account &nbsp;| Order Status | &nbsp;Wish Lists &nbsp;| Gift Certificates | &nbsp;View Cart &nbsp;&nbsp;| Sign in | Create an account</div>

<div class="abs brand"><span class="mark"></span>Geek Pagoda</div>

<nav class="abs nav-main">
  <a class="home" href="#">Home</a>
  <a href="#">Gifts by Category</a>
  <a href="#">What’s New?</a>
  <a href="#">Customer Services</a>
</nav>
<nav class="abs nav-sub">
  <span>Categories</span><span>Popular Brands</span><span>Shippings&amp;Returns</span><span>Contact Us</span>
</nav>

<div class="abs content"></div>

<aside class="abs side side-left">
  <label>Search</label>
  <div class="field"></div>
  <div style="text-align:right;margin-top:8px"><span class="btn">Go</span></div>
  <div class="cat-title">Categories:</div>
  <ul class="cat-list"><li>Candles</li><li>Decor</li><li>Key Covers</li><li>Kitchen</li><li>Magnets</li><li>Office</li><li>Toys</li></ul>
  <div class="divider"></div>
  <label>Your First Name:</label>
  <div class="field" style="width:125px"></div>
  <label style="margin-top:8px">Your Email:</label>
  <div class="field" style="width:127px"></div>
  <div style="margin-top:12px"><span class="btn">Submit</span></div>
</aside>

<div class="abs card" style="left:309px;top:388px;height:181px">
  <div class="ph" style="left:19px;top:33px;width:112px;height:34px;background:linear-gradient(90deg,#e33,#f93,#9c3,#39c,#96c)" role="img" aria-label="Row of colourful geometric magnet shapes"></div>
  <div class="info" style="top:112px">Geomagnetic Shaps<br>$10.75<br>Add To Cart</div>
</div>
<div class="abs card" style="left:483px;top:388px;height:177px">
  <div class="ph" style="left:20px;top:29px;width:112px;height:69px;background:linear-gradient(180deg,#b9c2cc,#d7a33a)" role="img" aria-label="Packaged set of emoticon key covers"></div>
  <div class="info" style="top:114px">KeyMoodies<br>$13.15<br>Add To Cart</div>
</div>
<div class="abs card" style="left:659px;top:388px;height:181px">
  <div class="ph" style="left:22px;top:23px;width:112px;height:71px;background:linear-gradient(180deg,#c9d2d8,#e6c84a)" role="img" aria-label="Packaged set of bird key covers"></div>
  <div class="info" style="top:117px">Cluckeys<br>$13.15<br>Add To Cart</div>
</div>
<div class="abs card" style="left:309px;top:598px;height:197px">
  <div class="ph" style="left:12px;top:5px;width:113px;height:113px;background:linear-gradient(135deg,#b9e6c8,#9fd3e6)" role="img" aria-label="Two translucent bendable figure toys"></div>
  <div class="info sm" style="top:138px">Mini-Zipman Glow in the Dark<br>$5.95<br>Choose Options</div>
</div>
<div class="abs card" style="left:483px;top:598px;height:197px">
  <div class="ph" style="left:11px;top:33px;width:112px;height:70px;background:linear-gradient(90deg,#e3262d,#7a4cc4,#f28a1c)" role="img" aria-label="Three colourful bendable figure toys"></div>
  <div class="info" style="top:130px;font-size:13px;line-height:16px">Large Zipman - Original<br>$10.75<br>Choose Options</div>
</div>

<aside class="abs side side-right">
  <h2>New Products</h2>
  <div class="np">Geomagnetic Shaps<br>$10.75<br>Add To Cart</div>
  <div class="np">KeyMoodies<br>$13.15<br>Add To Cart</div>
  <div class="np">Cluckeys<br>$13.15<br>Add To Cart</div>
  <div class="np">Mini-Zipman Glow in the Dark<br>$5.95<br>Choose Options</div>
  <div class="np" style="border:0">Large Zipman - Translucent<br>$10.75<br>Choose Options</div>
</aside>

<div class="abs footer">Contact us:</div>
</body>
</html>
```